Bluestone Advisory & Mgmt - Professional Business Cards

Hi!

I am a Real Estate Developer and Construction Consultant.

I have a lot of inspiration from previous designs and would be open to using the attached Designs as a starting point. I would like to see these styles incorporated into your designs.

I really need professional business card to go with it that includes my important info.

Look forward to seeing your designs!.

Target Market(s)

My Target market are building owners, lawyers, consultants.

Industry/Entity Type

Real Estate Development

Contact Information for Business Card

My Name: Dorian Pelkey
My Title: Principle
Company Name: Bluestone Advisory & Mgmt, LLC
Address: 348 West 71st Street, 9th FL New York, NY 10010
Mobile: 917.806.3971
Website: bam-hvx.example

Font styles to use
Serif
Sans Serif

Colors

Designer to choose colors to be used in the design.

Requirements
Must have
• Must incorporate the logo attached or have new that looks similar.
• Must use professional font that will be seen and judged by wealthy land owners and developers.
• Must incorporate some of the color green.
Should not have
• Photo's or pictures of people or buildings of any kind.

```html
<!DOCTYPE html>
<html lang="en">
<head>
<meta charset="utf-8">
<title>Bluestone Advisory &amp; Mgmt - Business Cards</title>
<link href="https://fonts.googleapis.com/css2?family=Lato:wght@400;700;900&family=Raleway:wght@400;600&display=swap" rel="stylesheet">
<style>
  :root {
    --bg: #1f1f1f;
    --green: #4cb87b;
    --grey: #9a9290;
    --ink: #3b3b44;
    --white: #ffffff;
    --rule: #5a5a6a;
  }
  * { margin: 0; padding: 0; box-sizing: border-box; }
  html, body { width: 1200px; height: 878px; overflow: hidden; background: var(--bg); }
  body { font-family: "Lato", Arial, sans-serif; position: relative; }

  .card {
    position: absolute;
    left: 250px;
    width: 700px;
    height: 400px;
    box-shadow: 0 6px 18px rgba(0,0,0,.5);
  }
  .card--front { top: 26px; background: var(--green); color: var(--white); }
  .card--back { top: 452px; background: var(--white); }

  .front-brand {
    position: absolute; left: 0; right: 0; top: 140px;
    text-align: center;
    font-weight: 900; font-size: 64px; letter-spacing: -1px;
  }
  .front-legal {
    position: absolute; left: 0; right: 0; top: 320px;
    text-align: center;
    font-size: 15px; letter-spacing: 1px; text-transform: uppercase;
  }

  .brand-block {
    position: absolute; left: 90px; top: 100px; width: 280px;
  }
  .brand-name {
    font-weight: 900; font-size: 52px; color: var(--green); letter-spacing: -1px; line-height: 1;
  }
  .brand-sub {
    font-family: "Raleway", Arial, sans-serif;
    margin-top: 10px; font-size: 21px; color: var(--grey); line-height: 1.1;
  }
  .divider {
    position: absolute; left: 390px; top: 100px; width: 1.5px; height: 135px; background: var(--rule);
  }
  .person {
    position: absolute; left: 412px; top: 98px;
  }
  .person-name { font-weight: 900; font-size: 34px; color: var(--green); line-height: 1; }
  .person-title { font-size: 16px; color: var(--ink); margin-top: 2px; }
  .contact-list { list-style: none; margin-top: 16px; }
  .contact-list li {
    display: flex; align-items: center; gap: 12px;
    font-size: 17px; color: var(--ink); height: 24px;
  }
  .contact-list svg { width: 15px; height: 15px; fill: var(--green); flex: none; }

  .footer-line {
    position: absolute; left: 0; right: 0; bottom: 56px;
    display: flex; justify-content: center; align-items: center; gap: 26px;
    font-size: 19px; color: var(--green);
  }
  .footer-line .sep { width: 1px; height: 20px; background: #b5b5b5; }
</style>
</head>
<body>
  <section class="card card--front">
    <div class="front-brand">Bluestone</div>
    <div class="front-legal">Bluestone Advisory &amp; Mgmt, LLC</div>
  </section>

  <section class="card card--back">
    <div class="brand-block">
      <div class="brand-name">Bluestone</div>
      <div class="brand-sub">Advisory Management</div>
    </div>
    <div class="divider"></div>
    <div class="person">
      <div class="person-name">Dorian Pelkey</div>
      <div class="person-title">Principle</div>
      <ul class="contact-list">
        <li>
          <svg viewBox="0 0 16 16" aria-hidden="true"><path d="M3.6 1.2l2.3 2.4-1.3 2a9 9 0 0 0 5.8 5.8l2-1.3 2.4 2.3-1.4 2.2C7.6 16 0 8.4 1.4 2.6z"/></svg>
          917.806.3971
        </li>
        <li>
          <svg viewBox="0 0 16 16" aria-hidden="true"><path d="M1 3h14v10H1zM2 4.2v.4l6 4 6-4v-.4z"/></svg>
          dorian@bam-hvx.example
        </li>
        <li>
          <svg viewBox="0 0 16 16" aria-hidden="true"><path d="M8 1a7 7 0 1 0 0 14A7 7 0 0 0 8 1zm0 1.5c.8 0 1.8 1.6 2.1 4H5.9C6.2 4.1 7.2 2.5 8 2.5zm-5.4 4h1.8a14 14 0 0 0 0 3H2.6a5.5 5.5 0 0 1 0-3zm3.3 0h4.2a12 12 0 0 1 0 3H5.9a12 12 0 0 1 0-3zm5.7 0h1.8a5.5 5.5 0 0 1 0 3h-1.8a14 14 0 0 0 0-3zM5.9 11h4.2c-.3 2.4-1.3 4-2.1 4s-1.8-1.6-2.1-4z"/></svg>
          www.bam-hvx.example
        </li>
      </ul>
    </div>
    <div class="footer-line">
      <span>Bluestone Advisory &amp; Mgmt, LLC</span>
      <span class="sep"></span>
      <span>348 West 71st ST. NY, NY 10010</span>
    </div>
  </section>
</body>
</html>
```